create clean, simple business card template

using the logo created now we need to create a simple, elegant business card design to suit

Industry/Entity Type

Business

Font styles to use
Other font styles liked:
• segoe ui

Requirements
Must have
• Front:
"Name:"
"Title:"
"Mobile:"
"email:"
and the logo

Back:
Logo
Nice to have
• Text in black but other graphics etc to match colours in logo as provided

```html
<!DOCTYPE html>
<html lang="en">
<head>
<meta charset="utf-8">
<title>K&amp;T Property – Business Card</title>
<link rel="stylesheet" href="https://fonts.googleapis.com/css2?family=Roboto+Slab:wght@400;600&display=swap">
<style>
  :root {
    --bg: #d6d6d6;
    --gold: #86703f;
    --dark: #3a332d;
    --white: #ffffff;
    --ink: #1c1a18;
    --faint: #eeeae3;
  }
  * { margin: 0; padding: 0; box-sizing: border-box; }
  html, body { width: 1200px; height: 985px; overflow: hidden; }
  body {
    background: var(--bg);
    font-family: "Roboto Slab", Georgia, serif;
    position: relative;
  }
  .card {
    position: absolute;
    left: 250px;
    width: 700px;
    height: 400px;
    border-radius: 26px;
    overflow: hidden;
    box-shadow: 0 14px 30px rgba(0,0,0,0.22);
  }
  .card-back { top: 55px; background: var(--gold); }
  .card-front { top: 530px; background: var(--white); }

  .brand { position: absolute; display: flex; align-items: center; gap: 14px; }
  .brand-dot { width: 26px; height: 26px; border-radius: 50%; flex: none; }
  .brand-name { font-weight: 600; white-space: nowrap; line-height: 1; }

  .card-back .brand { left: 50%; top: 50%; transform: translate(-50%, -50%); }
  .card-back .brand-dot { background: var(--white); width: 40px; height: 40px; }
  .card-back .brand-name { color: var(--white); font-size: 54px; }

  .name-tab {
    position: absolute; right: 0; bottom: 0;
    background: var(--dark); color: var(--white);
    padding: 10px 26px 12px 30px;
    border-top-left-radius: 22px;
    font-size: 15px; letter-spacing: 2px;
    white-space: nowrap;
  }
  .name-tab .divider { margin: 0 8px; opacity: .7; }
  .name-tab .role { letter-spacing: 1px; }

  .front-bands { position: absolute; left: 0; top: 0; }
  .watermark {
    position: absolute; left: 170px; top: 120px;
    color: var(--faint); white-space: nowrap;
  }
  .watermark-mark { display: block; font-size: 190px; font-weight: 600; line-height: 1; }
  .watermark-word { display: block; font-size: 40px; letter-spacing: 30px; margin-top: 4px; }

  .person { position: absolute; left: 180px; top: 24px; }
  .person-name { color: var(--gold); font-size: 30px; font-weight: 600; line-height: 1.1; }
  .person-title { color: var(--ink); font-size: 17px; font-weight: 600; margin-left: 40px; }

  .contact { position: absolute; left: 70px; top: 130px; list-style: none; }
  .contact li { color: var(--ink); font-size: 19px; line-height: 30px; height: 30px; white-space: nowrap; }

  .contact-icons { position: absolute; left: 14px; top: 132px; }

  .card-front .brand { right: 36px; top: 130px; }
  .card-front .brand-dot { background: var(--dark); }
  .card-front .brand-name { color: var(--gold); font-size: 36px; }
</style>
</head>
<body>

  <section class="card card-back" aria-label="Card back">
    <div class="brand">
      <span class="brand-dot"></span>
      <span class="brand-name">K&amp;T Property</span>
    </div>
    <div class="name-tab">TESSA ROWAN<span class="divider">|</span><span class="role">Director</span></div>
  </section>

  <section class="card card-front" aria-label="Card front">
    <div class="watermark" aria-hidden="true">
      <span class="watermark-mark">K&amp;T</span>
      <span class="watermark-word">PROPERTY</span>
    </div>

    <svg class="front-bands" width="700" height="400" viewBox="0 0 700 400" aria-hidden="true">
      <polygon points="0,0 150,0 110,70 0,70" fill="var(--gold)"/>
      <polygon points="0,70 110,70 60,150 55,270 0,290" fill="var(--dark)"/>
    </svg>

    <svg class="contact-icons" width="36" height="60" viewBox="0 0 36 60" aria-hidden="true">
      <rect x="8" y="2" width="22" height="22" rx="3" fill="var(--white)"/>
      <path d="M15 7 q-3 3 1 8 q4 5 8 3 l-1.5 -2.5 q-1.5 1 -3 -1 q-2 -2.5 -1 -3.5 z" fill="var(--dark)"/>
      <rect x="3" y="34" width="26" height="18" fill="var(--white)"/>
      <path d="M3 34 L16 45 L29 34" fill="none" stroke="var(--dark)" stroke-width="1.5"/>
    </svg>

    <div class="person">
      <div class="person-name">Tessa Rowan</div>
      <div class="person-title">Director</div>
    </div>

    <ul class="contact">
      <li class="contact-phone">010 555 019</li>
      <li class="contact-email">tessarowan@example.com</li>
    </ul>

    <div class="brand">
      <span class="brand-dot"></span>
      <span class="brand-name">K&amp;T Property</span>
    </div>
  </section>

</body>
</html>
```